Country House in Italy Needs a Business Card Design

We need a business card design for “Casale del Ginepro”, a modern concept of a Farm Holidays/Country House to be opened in central Italy.
Attached is the company logo you did for us in the past.
Please
- create a double-sided business card design
- on the back I would like to have the logo
- on the front the copy
Copy on card:
o Casale del Ginepro
o Address: Via Pontemurra, 14
Valdorsa (PG), Italy
o Website: www.casaledelginepro.it
o Email: info@casaledelginepro.it
o my name : Marisa
o my mobile phone number: +39 347 8123905
In the distribution of information keep in mind the possible inclusion also of a landline telephone number (currently not available / existing).
WE WOULD LIKE TO HAVE A MODERN, PROFFESIONAL, OUT OF THE BOX BUSINESS CARD. BE AS CREATIVE AS YOU WOULD LIKE.

```html
<!DOCTYPE html>
<html lang="it">
<head>
<meta charset="utf-8">
<title>Casale del Ginepro – Biglietto da visita</title>
<link href="https://fonts.googleapis.com/css2?family=Cormorant+Garamond:wght@400&family=Questrial&display=swap" rel="stylesheet">
<style>
  :root {
    --stage: #ecebe8;
    --paper: #ffffff;
    --ink: #3a3a3a;
    --ink-soft: #555555;
    --orange: #f47a1f;
    --orange-deep: #c85a0c;
    --orange-light: #ff9a3a;
    --brown: #8a5a2e;
  }
  * { margin: 0; padding: 0; box-sizing: border-box; }
  html, body { width: 1200px; height: 840px; overflow: hidden; }
  body { background: var(--stage); position: relative; font-family: "Questrial", "Century Gothic", sans-serif; }

  .card { position: absolute; box-shadow: 0 6px 18px rgba(0,0,0,0.18); }

  .card-back {
    left: 110px; top: 255px; width: 510px; height: 330px;
    background: radial-gradient(circle at 70% 35%, var(--orange-light) 0%, var(--orange) 45%, var(--orange-deep) 100%);
  }

  .card-front {
    left: 720px; top: 165px; width: 340px; height: 510px;
    background: var(--paper);
    color: var(--ink);
    display: flex; flex-direction: column; align-items: center;
    padding-top: 46px;
  }
  .brand { display: flex; flex-direction: column; align-items: center; }
  .brand-dot { width: 52px; height: 52px; border-radius: 50%; background: var(--orange); margin-bottom: 12px; }
  .brand-name { font-family: "Cormorant Garamond", Georgia, serif; font-size: 27px; color: var(--brown); letter-spacing: 0.3px; }
  .brand-tagline { font-size: 10px; letter-spacing: 1.6px; color: var(--orange); text-transform: uppercase; margin-top: 2px; }

  .contact { margin-top: 56px; width: 100%; padding-left: 92px; }
  .contact-name { font-size: 19px; margin-bottom: 12px; margin-left: 12px; }
  .contact-list { list-style: none; font-size: 12.5px; line-height: 17px; color: var(--ink-soft); }

  .address { margin-top: 26px; padding-left: 92px; width: 100%; font-size: 12.5px; color: var(--ink-soft); white-space: nowrap; }

  .social { margin-top: 34px; display: flex; gap: 5px; align-self: flex-end; margin-right: 58px; }
  .social span { width: 15px; height: 15px; background: var(--orange); display: block; }
</style>
</head>
<body>
  <div class="card card-back" role="img" aria-label="Back of card: orange radial mosaic of rounded tiles spiralling from the centre"></div>

  <div class="card card-front">
    <div class="brand">
      <div class="brand-dot"></div>
      <div class="brand-name">Casale del Ginepro</div>
      <div class="brand-tagline">Country House</div>
    </div>

    <div class="contact">
      <div class="contact-name">Marisa</div>
      <ul class="contact-list">
        <li>+39 347 8123905</li>
        <li>+39 0733 604118</li>
        <li>info@casaledelginepro.it</li>
        <li>www.casaledelginepro.it</li>
      </ul>
    </div>

    <div class="address">Via Pontemurra, 14 Valdorsa (PG), Italy</div>

    <div class="social" aria-label="Social links">
      <span></span><span></span><span></span>
    </div>
  </div>
</body>
</html>
```